Business card design needed for Automotive Reconditioning business

I have a logo design i just cant decide on the best color or layout for the business card, I will upload all the files so you can see all colors schemes we are considering. I have other file formats if needed let me know.

Target Market(s)

automotive dealerships

Contact Information for Business Card

HERE are the Descriptions and info needed on the card:
Interior Repair: Leather carpet burns panels dash Deoderize
Dealer products and Vin Verify
( spot for name and cell number) My name is Dorian Pelk phone 951 430-2158 Title COO www.BrolvexMotor.com

Font styles to use
Sans Serif
Other font styles liked:
• what ever you think looks best

Requirements
Must have
• Must be able to change the name and phone for employees

```html
<!DOCTYPE html>
<html lang="en">
<head>
<meta charset="utf-8">
<title>Brolvex Motor Reconditioning Corp. – Business Card</title>
<link rel="stylesheet" href="https://fonts.googleapis.com/css2?family=Montserrat:wght@400;600;700;800&display=swap">
<style>
  :root {
    --bg: #e7e9ec;
    --blue-deep: #1b3f8f;
    --blue: #1f6fc0;
    --blue-bright: #1e88d6;
    --red: #d8232a;
    --ink: #2f2f33;
    --grey: #6b6e73;
    --white: #ffffff;
  }
  * { margin: 0; padding: 0; box-sizing: border-box; }
  html, body { width: 1200px; height: 862px; overflow: hidden; }
  body {
    background: var(--bg);
    font-family: "Montserrat", sans-serif;
    position: relative;
  }
  .card {
    position: absolute;
    width: 600px;
    height: 343px;
    border-radius: 4px;
    overflow: hidden;
    box-shadow: 0 8px 24px rgba(0,0,0,.18);
  }

  /* Back side */
  .card-back {
    left: 110px; top: 56px;
    background: linear-gradient(160deg, var(--blue-bright) 0%, var(--blue) 45%, var(--blue-deep) 100%);
  }
  .back-name {
    position: absolute;
    left: 0; right: 0; top: 118px;
    text-align: center;
    font-weight: 800;
    font-size: 40px;
    line-height: 1.05;
    letter-spacing: 1px;
    color: rgba(18, 50, 120, .55);
    text-transform: uppercase;
  }
  .back-name small {
    display: block;
    font-size: 20px;
    letter-spacing: 1.5px;
  }
  .back-web {
    position: absolute;
    left: 0; right: 0; bottom: 52px;
    text-align: center;
    font-size: 15px;
    color: var(--white);
    letter-spacing: .3px;
  }
  .back-web .accent { color: var(--red); }

  /* Front side */
  .card-front {
    left: 490px; top: 460px;
    background: var(--white);
  }
  .front-name {
    position: absolute;
    left: 34px; top: 132px;
    width: 260px;
    font-weight: 800;
    font-size: 30px;
    line-height: 1.05;
    color: var(--blue);
    text-transform: uppercase;
  }
  .front-name small {
    display: block;
    font-size: 13.5px;
    letter-spacing: .6px;
    margin-top: 4px;
  }
  .divider {
    position: absolute;
    left: 316px; top: 64px;
    width: 1.5px; height: 120px;
    background: var(--blue-deep);
  }
  .contact {
    position: absolute;
    left: 334px; top: 60px;
  }
  .person {
    font-weight: 700;
    font-size: 20px;
    color: var(--blue-deep);
    letter-spacing: .5px;
  }
  .role {
    font-size: 12px;
    color: var(--grey);
    margin-top: 2px;
  }
  .rows { list-style: none; margin-top: 16px; }
  .rows li {
    display: flex;
    align-items: center;
    gap: 8px;
    font-size: 13px;
    color: var(--ink);
    height: 21px;
  }
  .rows svg { width: 14px; height: 14px; flex: none; }
  .wave { position: absolute; left: 0; bottom: 0; width: 600px; height: 343px; }
</style>
</head>
<body>

  <section class="card card-back" aria-label="Card back">
    <div class="back-name">Brolvex Motor<small>Reconditioning Corp.</small></div>
    <p class="back-web">www.<span class="accent">brolvexmotor</span>.com</p>
  </section>

  <section class="card card-front" aria-label="Card front">
    <svg class="wave" viewBox="0 0 600 343" aria-hidden="true">
      <path d="M0,336 C160,352 300,300 430,262 C510,238 560,226 600,222 L600,343 L0,343 Z" fill="var(--blue-bright)"/>
      <path d="M0,322 C160,338 300,286 430,248 C510,224 560,212 600,208" fill="none" stroke="var(--red)" stroke-width="6"/>
    </svg>

    <div class="front-name">Brolvex Motor<small>Reconditioning Corp.</small></div>
    <div class="divider"></div>

    <div class="contact">
      <p class="person">DORIAN PELK</p>
      <p class="role">COO</p>
      <ul class="rows">
        <li>
          <svg viewBox="0 0 14 14"><circle cx="7" cy="7" r="7" fill="var(--blue-deep)"/><path d="M4.5,3.5 L6,3.5 L6.5,5.5 L5.6,6.2 C6.1,7.3 6.8,8 7.8,8.4 L8.5,7.5 L10.5,8 L10.5,9.5 C7,10 4,7 4.5,3.5 Z" fill="#fff"/></svg>
          951 430-2158
        </li>
        <li>
          <svg viewBox="0 0 14 14"><circle cx="7" cy="7" r="7" fill="var(--blue-deep)"/><rect x="3.5" y="4.5" width="7" height="5" fill="none" stroke="#fff" stroke-width="1"/><path d="M3.5,4.5 L7,7.3 L10.5,4.5" fill="none" stroke="#fff" stroke-width="1"/></svg>
          info@brolvexmotor.com
        </li>
        <li>
          <svg viewBox="0 0 14 14"><circle cx="7" cy="7" r="7" fill="var(--blue-deep)"/><circle cx="7" cy="7" r="3.6" fill="none" stroke="#fff" stroke-width="1"/><ellipse cx="7" cy="7" rx="1.5" ry="3.6" fill="none" stroke="#fff" stroke-width="1"/><path d="M3.4,7 H10.6" stroke="#fff" stroke-width="1"/></svg>
          www.BrolvexMotor.com
        </li>
      </ul>
    </div>
  </section>

</body>
</html>
```